Business card for real estate agent / office

We're looking for a new business card. We want something that is pretty clean, modern and sleek. Something that also tells people that we are a new age company...cutting edge. Although real estate has been done a certain way the last 100 years, we have energy and vibrance. Company name is Silver Meadow Properties. info can be found here: http://www.smprealtyhub.example/

needs to include: Name, title, phone number, email. our license number also needs to be displayed somewhere.

Target Market(s)

25-55 homeowners or potential homeowners

Industry/Entity Type

Business

Contact Information for Business Card

we need business card designs for real estate agent / office

Font styles to use
Serif

Requirements
Must have
• needs to include: Name, title, phone number, email. our license number also needs to be displayed somewhere and company name.
Nice to have
• placement area for photo

```html
<!DOCTYPE html>
<html lang="en">
<head>
<meta charset="utf-8">
<title>Silver Meadow Properties — Business Card</title>
<link href="https://fonts.googleapis.com/css2?family=Open+Sans:wght@400;600;700&display=swap" rel="stylesheet">
<style>
  :root{
    --navy:#0b4870;
    --green:#62b946;
    --white:#ffffff;
    --paper:#eceff1;
    --ink:#0b4870;
  }
  *{box-sizing:border-box;margin:0;padding:0}
  html,body{width:1200px;height:1200px;overflow:hidden}
  body{background:var(--paper);font-family:"Open Sans",sans-serif;position:relative}
  .card{position:absolute;left:110px;width:980px;height:560px;overflow:hidden;box-shadow:0 6px 18px rgba(0,0,0,.18)}
  /* back side */
  .card--back{top:25px;background:var(--navy)}
  .back-band{position:absolute;left:0;right:0;top:170px;height:118px;background:var(--green);display:flex;align-items:center;justify-content:center}
  .back-rule{position:absolute;left:0;right:0;height:2px;background:var(--white)}
  .back-rule--top{top:152px}
  .back-rule--bottom{top:306px}
  .license{font-size:34px;color:var(--ink);letter-spacing:.5px;margin-left:60px}
  /* front side */
  .card--front{top:615px;background:var(--white)}
  .front-head{position:absolute;left:0;right:0;top:0;height:212px}
  .brand{position:absolute;left:70px;top:78px;display:flex;align-items:center;gap:16px}
  .brand-mark{width:34px;height:34px;background:var(--green)}
  .brand-name{font-size:34px;font-weight:700;color:var(--navy);line-height:1}
  .tagline{position:absolute;right:60px;top:58px;text-align:right;color:var(--navy);font-size:27px;line-height:1.35;letter-spacing:.5px;text-transform:uppercase}
  .front-body{position:absolute;left:0;right:0;top:212px;height:234px;background:var(--navy);color:var(--white)}
  .contacts{position:absolute;left:70px;top:72px;list-style:none;font-size:23px;line-height:1.32}
  .contacts li{display:flex;align-items:center;gap:12px}
  .contacts li.gap{margin-top:14px}
  .contacts svg{width:18px;height:18px;flex:none}
  .agent{position:absolute;right:60px;top:34px;text-align:right}
  .agent-name{font-size:40px;font-weight:700;letter-spacing:.5px;text-transform:uppercase}
  .agent-title{font-size:21px;margin-top:2px}
  .front-stripe{position:absolute;left:0;right:0;top:470px;height:62px;background:var(--green)}
</style>
</head>
<body>
  <section class="card card--back" aria-label="Card back">
    <div class="back-rule back-rule--top"></div>
    <div class="back-band"><span class="license">license number : xxxxxxxx</span></div>
    <div class="back-rule back-rule--bottom"></div>
  </section>

  <section class="card card--front" aria-label="Card front">
    <header class="front-head">
      <div class="brand">
        <span class="brand-mark"></span>
        <span class="brand-name">Silver Meadow Properties</span>
      </div>
      <p class="tagline">We greatly appreaiate<br>your referrals</p>
    </header>

    <div class="front-body">
      <ul class="contacts">
        <li>
          <svg viewBox="0 0 18 18" fill="none" stroke="currentColor" stroke-width="1.6"><rect x="5" y="1.5" width="8" height="15" rx="1.5"/><line x1="8" y1="13.5" x2="10" y2="13.5"/></svg>
          310.555.0142
        </li>
        <li>
          <svg viewBox="0 0 18 18" fill="currentColor"><path d="M4 2l3 3-1.5 2c1 2 2.5 3.5 4.5 4.5L12 10l3 3-2 2.5C7.5 15 3 10.5 2.5 5z"/></svg>
          424-555-0187
        </li>
        <li class="gap">
          <svg viewBox="0 0 18 18" fill="none" stroke="currentColor" stroke-width="1.4"><circle cx="9" cy="9" r="7.5"/><ellipse cx="9" cy="9" rx="3.2" ry="7.5"/><line x1="1.5" y1="9" x2="16.5" y2="9"/></svg>
          www.smprealtyhub.example
        </li>
        <li>
          <svg viewBox="0 0 18 18" fill="none" stroke="currentColor" stroke-width="1.5"><rect x="1.5" y="4" width="15" height="10"/><path d="M1.5 4L9 10l7.5-6"/></svg>
          info@smprealtyhub.example
        </li>
      </ul>
      <div class="agent">
        <h1 class="agent-name">Daniel Okafor</h1>
        <p class="agent-title">Real estate Broker, Realtor, MBA</p>
      </div>
    </div>

    <div class="front-stripe"></div>
  </section>
</body>
</html>
```